Bref créative
Modern stationary/business card design for KMR Interior Solutions
KMR Interior Solutions
Modern
Dolan Prewitt
VP
7428 B Fernvale
Lakemoor, TX 75990
dolan@cresthollowstone.com
www.cresthollowstone.com
We are open to tag lines so feel free to explore. I will give feedback to point you in the right direction.
Possibly a list of all the services we provide...
Granite, Quartz, Tile, Vinyl, Wood, Carpet, Mirrors, Cabinets, Hardware
I have more colors to choose from.

```html
<!DOCTYPE html>
<html lang="en">
<head>
<meta charset="utf-8">
<title>KMR Interior Solutions – Business Card</title>
<link rel="stylesheet" href="https://fonts.googleapis.com/css2?family=Open+Sans:wght@300;400&display=swap">
<style>
  :root {
    --bg: #e9e7e3;
    --card: #ffffff;
    --olive: #a39a36;
    --ink: #6b6b6b;
    --rule: #d6d3c8;
  }
  * { margin: 0; padding: 0; box-sizing: border-box; }
  html, body { width: 1200px; height: 988px; overflow: hidden; }
  body {
    background: var(--bg);
    font-family: "Open Sans", Arial, sans-serif;
    display: flex;
    flex-direction: column;
    align-items: center;
    justify-content: center;
    gap: 40px;
  }
  .card {
    width: 760px;
    height: 434px;
    background: var(--card);
    box-shadow: 0 6px 18px rgba(0,0,0,0.12);
  }

  /* Wordmark: one line, one colour, one weight */
  .brand {
    display: flex;
    align-items: center;
    gap: 14px;
    color: var(--olive);
    font-weight: 300;
    white-space: nowrap;
  }
  .brand__mark {
    width: 26px;
    height: 26px;
    background: var(--olive);
    flex: none;
  }
  .brand__name { font-size: 30px; line-height: 1; }

  /* Front */
  .card--front {
    display: flex;
    align-items: center;
    justify-content: center;
  }

  /* Back */
  .card--back {
    display: grid;
    grid-template-columns: 300px 1px 1fr;
    align-items: center;
  }
  .card--back .brand {
    flex-direction: column;
    gap: 12px;
    justify-self: center;
  }
  .card--back .brand__mark { width: 22px; height: 22px; }
  .card--back .brand__name { font-size: 22px; }
  .divider {
    width: 1px;
    height: 230px;
    background: var(--rule);
  }
  .contact { padding-left: 30px; color: var(--ink); }
  .contact__name { color: var(--olive); font-size: 22px; font-weight: 400; }
  .contact__title { font-size: 15px; margin: 2px 0 20px; }
  .contact__list { list-style: none; font-size: 15px; line-height: 1.6; }
  .contact__list li { display: flex; align-items: flex-start; gap: 10px; }
  .contact__list svg { flex: none; margin-top: 5px; }
  .contact__list .cont { padding-left: 24px; }
</style>
</head>
<body>

  <section class="card card--front">
    <div class="brand">
      <span class="brand__mark"></span>
      <span class="brand__name">KMR Interior Solutions</span>
    </div>
  </section>

  <section class="card card--back">
    <div class="brand">
      <span class="brand__mark"></span>
      <span class="brand__name">KMR Interior Solutions</span>
    </div>
    <div class="divider"></div>
    <div class="contact">
      <div class="contact__name">Dolan Prewitt</div>
      <div class="contact__title">VP</div>
      <ul class="contact__list">
        <li>
          <svg width="14" height="14" viewBox="0 0 14 14"><circle cx="7" cy="7" r="6" fill="none" stroke="#a39a36" stroke-width="1.5"/><circle cx="7" cy="6" r="2" fill="#a39a36"/></svg>
          <span>7428 B Fernvale</span>
        </li>
        <li class="cont">Lakemoor, TX 75990</li>
        <li>
          <svg width="14" height="14" viewBox="0 0 14 14"><circle cx="7" cy="7" r="7" fill="#a39a36"/><path d="M4.5 4 L6 4 L6.5 6 L5.6 6.6 Q6.4 8.2 7.6 8.8 L8.2 8 L10 8.5 L10 9.8 Q6.5 10.3 4.2 5.2 Z" fill="#fff"/></svg>
          <span>713-555-0142</span>
        </li>
        <li>
          <svg width="14" height="14" viewBox="0 0 14 14"><circle cx="7" cy="7" r="7" fill="#a39a36"/><rect x="5" y="3" width="4" height="8" rx="1" fill="#fff"/></svg>
          <span>832-555-0178</span>
        </li>
        <li>
          <svg width="14" height="14" viewBox="0 0 14 14"><circle cx="7" cy="7" r="6" fill="none" stroke="#a39a36" stroke-width="1.5"/><rect x="4" y="5" width="6" height="4" fill="#a39a36"/></svg>
          <span>713-555-0193</span>
        </li>
        <li>
          <svg width="14" height="14" viewBox="0 0 14 14"><circle cx="7" cy="7" r="6" fill="none" stroke="#a39a36" stroke-width="1.5"/><path d="M4 5 L7 7.5 L10 5" fill="none" stroke="#a39a36" stroke-width="1.3"/></svg>
          <span>dolan@cresthollowstone.com</span>
        </li>
        <li>
          <svg width="14" height="14" viewBox="0 0 14 14"><circle cx="7" cy="7" r="6" fill="none" stroke="#a39a36" stroke-width="1.5"/><path d="M1 7 H13 M7 1 Q10 7 7 13 Q4 7 7 1" fill="none" stroke="#a39a36" stroke-width="1"/></svg>
          <span>www.cresthollowstone.com</span>
        </li>
      </ul>
    </div>
  </section>

</body>
</html>
```